Corvane Real Estate Business Card

hello, we are a real estate company located in Los Angeles, california. we are a boutique, small company but we like a big corportate look. a simple, sleek, modern and progressive look. we would like the option of having a design that could include the real estate agents personal photo and also a design if the realtor desides not to have a photo. We also would like a hotizontal design.

Corvane Properties
3817 S Hadderly
Marlow Ridge, CA 90000
www.CorvaneRE.example

Gavin Prosk
Broker
BRE # 04829176
(555) 274-6390
gavin@corvanere.example

```html
<!DOCTYPE html>
<html lang="en">
<head>
<meta charset="UTF-8">
<title>Corvane Real Estate Business Card</title>
<link href="https://fonts.googleapis.com/css2?family=Roboto:wght@400;500&display=swap" rel="stylesheet">
<style>
  :root {
    --brand-blue: #174a86;
    --band-blue: #14457f;
    --ink: #1c1c1c;
    --paper: #f4f5f6;
    --backdrop: #e4e2df;
    --photo-top: #9aa58e;
    --photo-bottom: #2a2622;
    --white: #ffffff;
  }
  * { box-sizing: border-box; margin: 0; padding: 0; }
  html, body {
    width: 1200px; height: 720px; overflow: hidden;
    background: var(--backdrop);
    font-family: "Roboto", Arial, sans-serif;
  }
  .canvas {
    width: 1200px; height: 720px;
    display: flex; align-items: center; justify-content: center;
  }
  .card {
    position: relative;
    width: 1000px; height: 580px;
    background: var(--paper);
    overflow: hidden;
    box-shadow: 0 6px 24px rgba(0,0,0,0.18);
  }
  .rule {
    position: absolute; left: 0; right: 0; top: 272px;
    height: 5px; background: var(--brand-blue);
  }
  .band {
    position: absolute; left: 0; right: 0; top: 345px; bottom: 0;
    background: var(--band-blue);
  }
  .portrait {
    position: absolute; left: 64px; top: 62px;
    width: 236px; height: 340px;
    border: 3px solid var(--brand-blue);
    background: linear-gradient(180deg, var(--photo-top) 0%, #6f7563 45%, var(--photo-bottom) 100%);
  }
  .agent {
    position: absolute; left: 64px; width: 236px; top: 418px;
    text-align: center; color: var(--white);
  }
  .agent-name { font-size: 40px; font-weight: 500; line-height: 1.1; }
  .agent-title { font-size: 27px; font-weight: 400; margin-top: 4px; }
  .brand {
    position: absolute; left: 340px; top: 52px;
    display: flex; align-items: center; gap: 16px;
  }
  .brand-mark {
    width: 40px; height: 40px; border-radius: 50%;
    background: var(--brand-blue);
  }
  .brand-name {
    font-size: 52px; font-weight: 500; color: var(--brand-blue);
    letter-spacing: -0.5px;
  }
  .address {
    position: absolute; left: 340px; top: 158px;
    font-size: 31px; font-style: normal; color: var(--ink); line-height: 1.4;
  }
  .license {
    position: absolute; left: 340px; top: 292px;
    font-size: 27px; color: var(--brand-blue);
  }
  .contact {
    position: absolute; left: 450px; top: 400px;
    font-size: 27px; color: var(--white); line-height: 1.55;
  }
</style>
</head>
<body>
<div class="canvas">
  <section class="card">
    <div class="rule"></div>
    <div class="band"></div>

    <div class="portrait" role="img" aria-label="Portrait photo of broker Gavin Prosk in a dark suit"></div>

    <div class="agent">
      <p class="agent-name">Gavin Prosk</p>
      <p class="agent-title">Broker</p>
    </div>

    <div class="brand">
      <span class="brand-mark"></span>
      <span class="brand-name">Corvane Properties</span>
    </div>

    <address class="address">
      3817 S Hadderly<br>
      Marlow Ridge, CA 90000
    </address>

    <p class="license">BRE # 04829176</p>

    <div class="contact">
      <p>Phone: (555) 274-6390</p>
      <p>Email: gavin@corvanere.example</p>
    </div>
  </section>
</div>
</body>
</html>
```